Email Notification & Marketing Templates

I want to start with something like a newsletter or informational email, but i need Top Tips to Detect Phishing Scams. Something that i can send to users so they can follow it when receiving or exchanging emails. I will also need promotional items for my company that i can send to customers as well. It can be based on on our website PLVORIX.COM

Will also need:
newsletters
announcements
marketing emails
alerts
security notifications

Examples:Items such as Security Awareness Poster Series
Phishing Awareness
Password Security
Email Attachments
QR Code scams
Public WiFi safety

```html
<!DOCTYPE html>
<html lang="en">
<head>
<meta charset="utf-8">
<title>Stay Safe on Public WiFi – Plvorix</title>
<link rel="stylesheet" href="https://fonts.googleapis.com/css2?family=Inter:wght@400;500;600;700;800&display=swap">
<style>
  :root {
    --page-bg: #f1f4f5;
    --card-bg: #ffffff;
    --green: #2f8f1f;
    --green-dark: #1f6a14;
    --green-bright: #5fc13a;
    --green-fold: #15500d;
    --ink: #1d1f1e;
    --photo-a: #5e6a5c;
    --photo-b: #a7b39c;
    --photo-c: #3d4a3f;
  }
  * { box-sizing: border-box; margin: 0; padding: 0; }
  html, body {
    width: 1200px; height: 1200px; overflow: hidden;
    background: var(--page-bg);
    font-family: "Inter", Arial, sans-serif;
    color: var(--ink);
  }
  .email {
    position: absolute; left: 217px; top: 12px;
    width: 766px; height: 1176px;
    background: var(--card-bg);
  }
  .brand {
    position: absolute; top: 40px; left: 0; right: 0;
    display: flex; justify-content: center; align-items: center; gap: 16px;
  }
  .brand-name {
    font-size: 58px; font-weight: 800; color: var(--green);
    letter-spacing: -1px; line-height: 1;
  }
  .brand-mark { width: 40px; height: 40px; background: var(--green); }
  .headline {
    position: absolute; top: 160px; left: 0; right: 0;
    text-align: center; font-size: 52px; font-weight: 700;
    color: var(--green); letter-spacing: -0.5px;
  }
  .hero {
    position: absolute; top: 252px; left: 0; width: 766px; height: 383px;
    background: radial-gradient(circle at 40% 55%, rgba(120, 220, 110, 0.55) 0, rgba(120, 220, 110, 0.15) 28%, transparent 45%),
                linear-gradient(120deg, var(--photo-c), var(--photo-a) 45%, var(--photo-b));
  }
  .section-banner {
    position: absolute; height: 51px; color: #fff;
    font-weight: 600; font-size: 29px;
    display: flex; align-items: center;
  }
  .tips-banner {
    top: 669px; left: 0; width: 515px; padding-left: 62px;
    background: linear-gradient(90deg, var(--green-bright), var(--green) 60%);
    clip-path: polygon(0 0, 100% 0, 94% 100%, 0 100%);
  }
  .fold { position: absolute; width: 16px; height: 14px; background: var(--green-fold); }
  .fold-left { left: 0; clip-path: polygon(0 0, 100% 0, 100% 100%); }
  .fold-right { right: 0; clip-path: polygon(0 0, 100% 0, 0 100%); }
  .tips-fold { top: 720px; }
  .tips-list { position: absolute; top: 735px; left: 60px; list-style: none; }
  .tip {
    display: flex; align-items: center; gap: 16px;
    height: 48px; font-size: 25px; font-weight: 400;
  }
  .tip-icon { width: 34px; height: 34px; flex: none; }
  .divider {
    position: absolute; top: 908px; left: 0; width: 766px; height: 8px;
    background: linear-gradient(90deg, var(--green-bright), var(--green));
  }
  .solutions-banner {
    top: 934px; left: 0; width: 766px; justify-content: center;
    background: linear-gradient(90deg, var(--green-dark), var(--green) 50%, var(--green-dark));
    font-size: 31px;
  }
  .solutions-fold { top: 985px; }
  .solutions-copy {
    position: absolute; top: 1000px; left: 0; right: 0;
    text-align: center; font-size: 25px; line-height: 1.2;
  }
  .cta {
    position: absolute; top: 1081px; left: 205px; width: 356px; height: 57px;
    background: var(--green); color: #fff; border-radius: 4px;
    display: flex; align-items: center; justify-content: center;
    font-size: 23px; font-weight: 600; letter-spacing: 0.3px;
  }
</style>
</head>
<body>
<main class="email">
  <header class="brand">
    <span class="brand-name">Plvorix Networks</span>
    <span class="brand-mark"></span>
  </header>

  <h1 class="headline">Stay Safe on Public WiFi</h1>

  <div class="hero" role="img" aria-label="Person working on a laptop at a café table, surrounded by a glowing green protective dome with a padlock shield on the screen"></div>

  <div class="section-banner tips-banner">Tips for Secure Public WiFi:</div>
  <span class="fold fold-left tips-fold"></span>

  <ul class="tips-list">
    <li class="tip">
      <svg class="tip-icon" viewBox="0 0 34 34" fill="none" stroke="#2f8f1f" stroke-width="2">
        <circle cx="14" cy="10" r="6"/>
        <path d="M3 30c0-7 5-11 11-11 3 0 5 1 7 2"/>
        <circle cx="25" cy="25" r="6"/>
        <path d="M25 22v4M25 28v0.5"/>
      </svg>
      <span>1. Avoid Sensitive Logins &amp; Transactions</span>
    </li>
    <li class="tip">
      <svg class="tip-icon" viewBox="0 0 34 34" fill="none" stroke="#2f8f1f" stroke-width="2">
        <path d="M17 3l12 5v8c0 8-5 13-12 15C10 29 5 24 5 16V8z"/>
        <rect x="12" y="15" width="10" height="8" rx="1"/>
        <path d="M14 15v-3a3 3 0 016 0v3"/>
      </svg>
      <span>2. Always Use a Reliable VPN (Virtual Private Network)</span>
    </li>
    <li class="tip">
      <svg class="tip-icon" viewBox="0 0 34 34" fill="none" stroke="#2f8f1f" stroke-width="2">
        <path d="M3 13a19 19 0 0126 0M7 18a13 13 0 0118 0M11 23a7 7 0 0110 0"/>
        <circle cx="16" cy="28" r="1.5" fill="#2f8f1f"/>
        <rect x="22" y="24" width="10" height="8" rx="1"/>
        <path d="M24 24v-2a3 3 0 016 0v2"/>
      </svg>
      <span>3. Verify Network Names Before Connecting</span>
    </li>
  </ul>

  <div class="divider"></div>

  <div class="section-banner solutions-banner">Plvorix Cybersecurity Solutions</div>
  <span class="fold fold-left solutions-fold"></span>
  <span class="fold fold-right solutions-fold"></span>

  <p class="solutions-copy">Comprehensive protection for your business data<br>and network, anywhere.</p>

  <a class="cta">PROTECT YOUR BUSINESS</a>
</main>
</body>
</html>
```